Flyer-Design für Immobilienmakler
Meine Vorgaben wurden Umgesetzt aber es wurden auch gute eigene Ideen eingebracht. Änderungswünsche wurden schnell umgesetzt. Danke.
Zielgruppe
Mein Mann und ich sind Immobilienmakler und benötigen immer wieder neue Akquiseflyer.
Diesmal sollen die älteren Immobilienbesitzer angesprochen werde welche ihre Immobilie verkaufen möchten da z.b. die Kinder aus dem Haus sind und etwas kleineres benötigt wird, oder die Wohnung im DG soll verkauft werden weil eine Wohnung im EG sinnvoll wäre.
Frühjahrsaktion: keine Provision für den Verkäufer
Aufgabenstellung
Ca. Din A5, Voder und Rückseite
Als Postkarte. Porto zahlt Empfänger
Der Flyer soll von den Farben her zu den vorherigen passen

```html
<!DOCTYPE html>
<html lang="de">
<head>
<meta charset="utf-8">
<title>Akquise-Postkarte Nord-Immobilien Wendlinger</title>
<link href="https://fonts.googleapis.com/css2?family=Nunito+Sans:wght@400;600;700;800&display=swap" rel="stylesheet">
<style>
  :root {
    --blue: #1f4a7c;
    --blue-dark: #173a63;
    --gold: #b0893a;
    --line: #7d9cc0;
    --text: #2c3440;
    --grey: #8a9099;
    --page: #e9e9ea;
    --card: #ffffff;
  }
  * { margin: 0; padding: 0; box-sizing: border-box; }
  html, body { width: 1200px; height: 2998px; overflow: hidden; }
  body {
    background: var(--page);
    font-family: "Nunito Sans", Arial, sans-serif;
    color: var(--text);
    position: relative;
  }
  .card {
    position: absolute;
    left: 90px;
    width: 1020px;
    height: 507px;
    background: var(--card);
    box-shadow: 0 4px 18px rgba(0,0,0,0.14);
    overflow: hidden;
  }
  .card--front { top: 952px; }
  .card--back { top: 1538px; }

  /* ---------- Front: reply side ---------- */
  .reply {
    position: absolute; left: 34px; top: 30px; width: 250px;
    font-size: 14px; line-height: 1.38;
  }
  .reply__title { color: var(--blue); font-weight: 800; font-size: 15.5px; margin-bottom: 10px; }
  .reply__text { color: var(--blue-dark); margin-bottom: 14px; }
  .reply__own { color: var(--blue-dark); }
  .reply__choices { display: flex; gap: 14px; margin: 4px 0 16px; color: var(--blue-dark); }
  .reply__choices span { display: flex; align-items: center; gap: 5px; }
  .checkbox { width: 13px; height: 13px; border: 1.5px solid var(--blue); display: inline-block; }
  .field {
    height: 38px; border-bottom: 1.5px solid var(--line);
    font-size: 11px; color: var(--grey); padding-top: 8px;
  }
  .divider {
    position: absolute; left: 296px; top: 30px; width: 2px; height: 445px; background: var(--gold); opacity: .7;
  }
  .stamp {
    position: absolute; left: 380px; top: 32px; width: 96px; height: 114px;
    border: 1.5px solid var(--text);
    display: flex; align-items: center; justify-content: center; text-align: center;
    font-size: 15px; line-height: 1.25;
  }
  .postmark { position: absolute; left: 312px; top: 214px; font-size: 14px; }
  .postmark__brand { font-weight: 800; }
  .postmark__mode { font-weight: 800; font-style: italic; font-size: 13px; letter-spacing: .5px; }
  .recipient { position: absolute; left: 312px; top: 296px; font-size: 15px; line-height: 1.35; }
  .recipient__name { color: var(--blue); font-weight: 800; margin-bottom: 14px; }

  .front-photo {
    position: absolute; left: 520px; top: 32px; width: 455px; height: 444px;
    background:
      linear-gradient(to bottom, rgba(255,255,255,0) 55%, rgba(255,255,255,.92) 88%, #fff 100%),
      linear-gradient(120deg, #d9d4cc 0%, #b9aea3 35%, #e6e1da 60%, #c5cdd6 100%);
  }
  .banner {
    position: absolute; color: #fff; font-weight: 600; text-transform: none;
    padding: 8px 16px 8px 28px; font-size: 17.5px; line-height: 1.2;
  }
  .banner::before {
    content: ""; position: absolute; left: 8px; top: 10px; width: 12px; height: 12px;
    background: #fff; border-radius: 50%;
  }
  .banner--service { background: var(--blue); left: 750px; top: 86px; width: 250px; text-transform: uppercase; }
  .banner--offer { background: var(--gold); left: 750px; top: 166px; width: 262px; }
  .banner--offer strong { text-transform: uppercase; font-weight: 700; }
  .slogan {
    position: absolute; left: 540px; top: 352px; width: 435px; text-align: right;
    color: var(--blue); font-weight: 800; font-size: 26px; line-height: 1.15;
  }
  .slogan small { font-size: 17px; font-weight: 700; }
  .slogan .big { font-size: 32px; }

  /* ---------- Back: info side ---------- */
  .back-photo {
    position: absolute; left: 32px; top: 32px; width: 458px; height: 444px;
    background:
      linear-gradient(to bottom, rgba(255,255,255,0) 0%, rgba(255,255,255,0) 40%, rgba(255,255,255,.95) 62%, #fff 100%),
      radial-gradient(ellipse at 45% 35%, #c8ccd2 0%, #e3e5e8 45%, #f4f4f4 100%);
  }
  .web-tag {
    position: absolute; left: 18px; top: 36px; background: var(--blue); color: #fff;
    font-weight: 800; font-size: 17px; padding: 7px 20px 7px 24px;
  }
  .claim {
    position: absolute; left: 40px; top: 238px; width: 440px; text-align: center;
    color: var(--gold); font-weight: 700; font-size: 18px; line-height: 1.3;
  }
  .claim b { font-size: 23px; font-weight: 800; }
  .info-box {
    position: absolute; left: 520px; top: 30px; width: 480px; height: 262px;
    background: var(--blue); color: #fff; padding: 18px 22px;
    font-size: 14px; line-height: 1.45;
  }
  .info-box p + p { margin-top: 14px; }
  .contact { position: absolute; left: 540px; top: 318px; font-size: 14px; color: var(--text); }
  .contact__title { color: var(--blue); font-weight: 800; margin-bottom: 6px; }
  .contact__row { display: flex; align-items: center; gap: 8px; line-height: 1.6; }
  .contact__row svg { width: 13px; height: 13px; fill: var(--gold); }
  .brand {
    position: absolute; left: 800px; top: 380px; width: 190px; text-align: center;
    color: var(--blue); font-weight: 800; font-size: 20px; line-height: 1.15;
  }
  .brand__square { display: block; width: 34px; height: 34px; background: var(--gold); margin: 0 auto 8px; }
</style>
</head>
<body>

<section class="card card--front" aria-label="Postkarte Antwortseite">
  <div class="reply">
    <h2 class="reply__title">Bitte kontaktieren Sie uns:</h2>
    <p class="reply__text">Wir planen den Verkauf unserer Immobilie und würden gerne mehr über Ihren Service wissen. Bitte kontaktieren Sie uns, damit wir einen unverbindlichen Beratungstermin vereinbaren können.</p>
    <p class="reply__own">Wir besitzen …</p>
    <div class="reply__choices">
      <span><i class="checkbox"></i>ein Haus</span>
      <span><i class="checkbox"></i>eine Wohnung</span>
    </div>
    <div class="field">Name</div>
    <div class="field">Telefon</div>
    <div class="field">Straße</div>
    <div class="field">PLZ, Ort</div>
    <div class="field">E-Mail</div>
  </div>

  <div class="divider"></div>

  <div class="stamp">Entgelt<br>zahlt<br>Empfänger</div>

  <div class="postmark">
    <div class="postmark__brand">Briefpost</div>
    <div class="postmark__mode">ANTWORT</div>
  </div>

  <address class="recipient" style="font-style:normal">
    <div class="recipient__name">Nord-Immobilien<br>Wendlinger GmbH</div>
    Lindenweg 7<br>73001 Musterau
  </address>

  <div class="front-photo" role="img" aria-label="Foto: lächelndes älteres Ehepaar entspannt auf einem Sofa zu Hause"></div>

  <div class="banner banner--service">Immobilienservice<br>für Eigentümer</div>
  <div class="banner banner--offer"><strong>Frühjahrsaktion:</strong> keine<br>Provision für den Verkäufer</div>

  <p class="slogan">Sie <small>entspannen</small> und <small>wir</small><br>kümmern uns <small>für</small> <span class="big">Sie!</span></p>
</section>

<section class="card card--back" aria-label="Postkarte Informationsseite">
  <div class="back-photo" role="img" aria-label="Foto: Hausmodell mit Bäumen auf einem Schreibtisch, Hand mit Stift im Hintergrund"></div>
  <div class="web-tag">www.nordimmo-wendlinger.de</div>
  <p class="claim">Wir stehen Ihnen nicht nur mit<br><b>Fachkompetenz,</b> sondern auch<br><b>ehrlich, fair</b> und <b>zuverlässig</b> zur Seite.</p>

  <div class="info-box">
    <p>Sie suchen den passenden Käufer für Ihre Immobilie?<br>Sie wollen ein Haus oder eine Wohnung verkaufen?</p>
    <p>Dann ist Nord-Immobilien Wendlinger in Musterau Ihr kompetenter Ansprechpartner. Mit vielen Jahren Erfahrung als Immobilienmakler widmen wir uns der Suche nach dem Suchenden. Wir finden für Ihr Objekt den geeigneten Käufer – auch wenn Sie bisher vielleicht der Meinung waren, Ihre Immobilie sei nicht ganz einfach zu vermitteln oder zu speziell in ihrer Erscheinung.</p>
  </div>

  <div class="contact">
    <div class="contact__title">Kontakt</div>
    <div class="contact__row">
      <svg viewBox="0 0 24 24" aria-hidden="true"><path d="M6.6 10.8a15.1 15.1 0 0 0 6.6 6.6l2.2-2.2c.3-.3.7-.4 1-.2 1.1.4 2.3.6 3.6.6.6 0 1 .4 1 1V20c0 .6-.4 1-1 1A17 17 0 0 1 3 4c0-.6.4-1 1-1h3.5c.6 0 1 .4 1 1 0 1.3.2 2.5.6 3.6.1.3 0 .7-.2 1z"/></svg>
      07000 / 12 34 56
    </div>
    <div class="contact__row">
      <svg viewBox="0 0 24 24" aria-hidden="true"><path d="M2 5h20v14H2z M2 5l10 8 10-8" fill="none" stroke="#b0893a" stroke-width="2.4"/></svg>
      info@nordimmo-wendlinger.de
    </div>
  </div>

  <div class="brand"><span class="brand__square"></span>Nord-Immobilien<br>Wendlinger</div>
</section>

</body>
</html>
```